Root Crate Filtration Label Design

Need a sticker or label design for our Root Crate to fit an 8x6" area.

UPDATE 9/21/2015:
We eliminated some text and would like to see only the following on the label:

Root Crate Contains:

- Terrestrial Soil
- Lake Sediment
- Organic Matter
- Natural Bacteria
- Minerals & Trace Elements

"STAY RIVER CALM"

We would love to see an illustration of graphic of the outline of our Root Crate (Black plastic box) showing the soil on the inside which is brown and a thin layer of foam on top of the soil inside the box. On top of the box a layer of natural gravel and the plant roots shown growing through the gravel into the soil inside of the box.

Watch this video to get an idea of how the Root Crate fits in an aquarium under a layer of gravel: https://www.clipvaultly.com/watch?t=92&v=qrTm4kLx8Wd
Updates

Target Market(s)

Customers in Retail Stores

Industry/Entity Type

Pet

Font styles to use
Sans Serif

Colors
9bcb3c
0393ce
0255a3
33b8a4
cadf82
add136
86cfc7
cfeae6
eaf2ce

Requirements
Must have
• Stay River Calm and most of the Text - Text can be changed slightly or simplified
Nice to have
• I have attached a picture of a "FRESHWATER Fish Scene" we like.
Should not have
• NOT Too busy - Trying to keep it as simple as possible - Natural Earthy Colors - Realistic Drawings. DO NOT ADD Marine Fish or other MARINE life. This is strictly for FRESHWATER FISH.

```html
<!DOCTYPE html>
<html lang="en">
<head>
<meta charset="utf-8">
<title>Root Crate Filtration Labels</title>
<link rel="stylesheet" href="https://fonts.googleapis.com/css2?family=Montserrat:wght@500;600;700;800&family=Roboto:wght@400;500&display=swap">
<style>
  :root {
    --stage: #ecebe7;
    --deep-blue: #0255a3;
    --sky-blue: #0393ce;
    --navy: #06306e;
    --aqua: #86cfc7;
    --mist: #cfeae6;
    --leaf: #add136;
    --lime: #cadf82;
    --white: #ffffff;
  }
  * { box-sizing: border-box; margin: 0; padding: 0; }
  html, body { width: 857px; height: 1200px; overflow: hidden; }
  body {
    background: var(--stage);
    font-family: "Roboto", Arial, sans-serif;
    position: relative;
  }
  .label { position: absolute; }
  .label-shape { position: absolute; inset: 0; }
  .label-top { left: 156px; top: 60px; width: 545px; height: 470px; }
  .label-bottom { left: 136px; top: 630px; width: 585px; height: 545px; }

  .brand {
    position: absolute; left: 0; right: 0; text-align: center;
    font-family: "Montserrat", Arial, sans-serif;
    font-weight: 800; color: var(--sky-blue); line-height: 1;
  }
  .label-bottom .brand { color: var(--mist); }
  .brand-name { display: block; letter-spacing: 1px; }
  .brand-sub { display: block; letter-spacing: 4px; }
  .label-top .brand { top: 62px; }
  .label-top .brand-name { font-size: 62px; }
  .label-top .brand-sub { font-size: 26px; margin-top: 6px; }
  .label-bottom .brand { top: 52px; }
  .label-bottom .brand-name { font-size: 62px; }
  .label-bottom .brand-sub { font-size: 20px; letter-spacing: 12px; margin-top: 8px; }

  .contents {
    position: absolute; list-style: none;
    font-family: "Montserrat", Arial, sans-serif; font-weight: 500;
  }
  .label-top .contents {
    left: 115px; top: 196px; width: 330px;
    display: grid; grid-template-columns: 120px 1fr; column-gap: 20px;
    color: var(--white); font-size: 13px; line-height: 1.3;
    white-space: nowrap;
  }
  .label-bottom .contents {
    left: 15px; right: 15px; top: 228px; text-align: center;
    color: var(--navy); font-size: 18px; line-height: 1.4;
    white-space: nowrap;
  }
  .label-bottom .contents li { display: inline; }
  .label-bottom .contents li + li::before { content: " | "; }
  .label-bottom .contents li:nth-child(3)::after { content: "\A"; white-space: pre; }
  .label-bottom .contents li:nth-child(4)::before { content: none; }

  .approach {
    position: absolute; left: 0; right: 0; text-align: center;
    font-size: 10px; line-height: 1.3;
  }
  .label-top .approach { top: 254px; color: var(--mist); padding: 0 120px; }
  .label-bottom .approach { top: 290px; color: var(--navy); padding: 0 140px; }

  .key-line {
    position: absolute; left: 0; right: 0; text-align: center;
    font-family: "Montserrat", Arial, sans-serif; font-weight: 600;
    text-transform: uppercase; line-height: 1.15;
  }
  .label-top .key-line { top: 286px; color: var(--leaf); font-size: 18px; }
  .label-bottom .key-line { top: 346px; color: var(--white); font-size: 17px; }

  .slogan {
    position: absolute; left: 0; right: 0; text-align: center;
    font-family: "Montserrat", Arial, sans-serif; font-weight: 500;
    color: var(--white); letter-spacing: 1px; line-height: 1.1;
  }
  .label-top .slogan { top: 336px; font-size: 30px; }
  .label-bottom .slogan { top: 402px; font-size: 32px; }

  .scene-fill { position: absolute; border-radius: 6px; }
  .label-top .scene-fill {
    left: 40px; right: 40px; top: 378px; height: 58px;
    background: linear-gradient(180deg, rgba(3,147,206,0) 0%, rgba(51,184,164,0.45) 100%);
  }
  .label-bottom .scene-fill {
    left: 30px; right: 30px; top: 462px; height: 62px;
    background: linear-gradient(180deg, rgba(134,207,199,0) 0%, rgba(2,85,163,0.45) 100%);
  }
  .bubbles-fill {
    position: absolute; left: 30px; top: 330px; width: 90px; height: 110px;
    background: radial-gradient(circle at 50% 50%, rgba(255,255,255,0.35), rgba(255,255,255,0) 70%);
  }
</style>
</head>
<body>

<section class="label label-top">
  <svg class="label-shape" viewBox="0 0 545 470" aria-hidden="true">
    <defs>
      <linearGradient id="topHead" x1="0" y1="0" x2="0" y2="1">
        <stop offset="0" stop-color="#ffffff"/>
        <stop offset="1" stop-color="#cfeae6"/>
      </linearGradient>
      <linearGradient id="topBody" x1="0" y1="0" x2="0" y2="1">
        <stop offset="0" stop-color="#0393ce"/>
        <stop offset="0.35" stop-color="#0255a3"/>
        <stop offset="1" stop-color="#0470b8"/>
      </linearGradient>
    </defs>
    <path d="M0 0 H545 V440 Q470 470 380 450 Q280 428 180 456 Q90 478 0 445 Z" fill="url(#topBody)"/>
    <path d="M0 0 H545 V160 Q450 200 340 170 Q230 142 130 182 Q60 206 0 180 Z" fill="url(#topHead)"/>
    <path d="M0 180 Q60 206 130 182 Q230 142 340 170 Q450 200 545 160" fill="none" stroke="#86cfc7" stroke-width="4"/>
  </svg>
  <h1 class="brand"><span class="brand-name">ROOT CRATE</span><span class="brand-sub">FILTRATION</span></h1>
  <ul class="contents">
    <li>Terrestrial Soil</li><li>Organic Matter</li>
    <li>Lake Sediment</li><li>Natural Bacteria</li>
    <li></li><li>Minerals &amp; Trace Elements</li>
  </ul>
  <p class="approach">A Natural Approach for Thriving Fish &amp; Plants in Planted Tanks with stable roots and steady water conditions</p>
  <p class="key-line">Live aquatic plants &amp; soil are key to<br>a thriving freshwater aquarium</p>
  <p class="slogan">STAY RIVER CALM</p>
  <div class="scene-fill" role="img" aria-label="Freshwater plants and a small fish along the bottom edge"></div>
</section>

<section class="label label-bottom">
  <svg class="label-shape" viewBox="0 0 585 545" aria-hidden="true">
    <defs>
      <linearGradient id="botHead" x1="0" y1="0" x2="0" y2="1">
        <stop offset="0" stop-color="#0255a3"/>
        <stop offset="1" stop-color="#0393ce"/>
      </linearGradient>
      <linearGradient id="botBody" x1="0" y1="0" x2="0" y2="1">
        <stop offset="0" stop-color="#cfeae6"/>
        <stop offset="0.4" stop-color="#86cfc7"/>
        <stop offset="1" stop-color="#0393ce"/>
      </linearGradient>
    </defs>
    <path d="M0 10 Q140 0 300 12 Q450 22 585 6 V530 Q450 548 300 532 Q150 516 0 540 Z" fill="url(#botBody)"/>
    <path d="M0 10 Q140 0 300 12 Q450 22 585 6 V170 Q460 210 330 180 Q190 150 70 200 Q30 214 0 205 Z" fill="url(#botHead)"/>
    <path d="M0 205 Q30 214 70 200 Q190 150 330 180 Q460 210 585 170" fill="none" stroke="#ffffff" stroke-width="14"/>
  </svg>
  <h2 class="brand"><span class="brand-name">ROOT CRATE</span><span class="brand-sub">FILTRATION</span></h2>
  <ul class="contents">
    <li>Terrestrial Soil</li><li>Lake Sediment</li><li>Organic Matter</li><li>Natural Bacteria</li><li>Minerals &amp; Trace Elements</li>
  </ul>
  <p class="approach">A Natural Approach for Thriving Fish &amp; Plants in Planted Tanks with stable roots and steady water conditions</p>
  <div class="bubbles-fill" role="img" aria-label="Rising air bubbles"></div>
  <p class="key-line">Live aquatic plants &amp; soil are key to a<br>thriving freshwater aquarium</p>
  <p class="slogan">STAY RIVER CALM</p>
  <div class="scene-fill" role="img" aria-label="Freshwater plants and small fish along the bottom edge"></div>
</section>

</body>
</html>
```